HALVERN BRIDGE LIMITED CALENDAR 2018

We need an innovative calendar design for our company for 2018. to give a brief description of our company:
"Halvern Bridge was founded in 2016 to provide a wide range of management consultancy and advisory services to small and medium-sized companies operating in consumer-driven sectors. With more than 300 years of cumulative investment and advisory experience among our sector-focused seasoned professionals, we advise management teams on an aggregate of $850m worth of investments operating in the healthcare, education, food and beverage and logistics sectors within the MENASEA region; the region of our expertise."
We want the design to include the following 12 countries for each month:
1. UAE 2. Saudi Arabia 3. Kuwait 4. Bahrain 5. Qatar 6. Oman 7. Jordan 8. Egypt 9. Singapore 10. Malaysia 11. Thailand 12. Indonesia
The description/design for each month must include each country's economic growth, Per Capita Income, GDP, etc. That is what we wish for the final design for each month to communicate as our company is in to a wide range of Investment management and Advisory Services
Target Market(s)
FINANCIAL SERVICES AND CONSULTING
Industry/Entity Type
Financial Service
Font styles to use
Colors
Designer to choose colors to be used in the design.
Look and feel

```html
<!DOCTYPE html>
<html lang="en">
<head>
<meta charset="utf-8">
<title>Halvern Bridge Calendar 2018 – June</title>
<link href="https://fonts.googleapis.com/css2?family=Open+Sans:ital,wght@0,400;0,600;0,700;1,400;1,700&family=Pinyon+Script&display=swap" rel="stylesheet">
<style>
  :root {
    --gold: #b8922a;
    --gold-light: #d4ae4a;
    --navy: #1d2740;
    --navy-deep: #141b30;
    --maroon: #7a1f2b;
    --ink: #1e1e1e;
    --grey-cell: #e6e6e6;
    --grey-line: #cfcfcf;
    --white: #ffffff;
  }
  * { margin: 0; padding: 0; box-sizing: border-box; }
  html, body { width: 1200px; height: 847px; overflow: hidden; background: var(--white); }
  body { font-family: "Open Sans", Arial, sans-serif; color: var(--ink); }
  .calendar-page { position: relative; width: 1200px; height: 847px; overflow: hidden; background: var(--white); }
  .shapes { position: absolute; inset: 0; width: 1200px; height: 847px; }

  .month-header { position: absolute; left: 676px; top: 66px; width: 520px; height: 80px; }
  .month-header .year { position: absolute; left: 0; top: 0; font-size: 54px; font-weight: 700; color: var(--gold); line-height: 1; }
  .month-header .rule { position: absolute; left: 0; top: 72px; width: 348px; height: 3px; background: var(--gold); }
  .month-header .month { position: absolute; left: 366px; top: -8px; font-family: "Pinyon Script", cursive; font-size: 72px; color: var(--maroon); line-height: 1; }

  .month-grid { position: absolute; left: 667px; top: 180px; width: 451px; border-collapse: collapse; table-layout: fixed; }
  .month-grid th { height: 26px; background: var(--grey-cell); color: var(--maroon); font-size: 15px; font-weight: 700; text-align: left; padding-left: 6px; border-right: 2px solid var(--white); }
  .month-grid td { height: 47px; vertical-align: top; text-align: left; padding: 4px 0 0 6px; font-size: 17px; font-weight: 700; border-bottom: 1px solid var(--grey-line); border-right: 2px solid var(--white); }
  .month-grid .weekend-col { background: var(--grey-cell); }

  .brand { position: absolute; left: 692px; top: 514px; font-size: 26px; font-weight: 700; letter-spacing: 3px; color: var(--gold); display: flex; align-items: center; gap: 10px; line-height: 1.2; }
  .brand .mark { width: 14px; height: 14px; background: var(--gold); }
  .about { position: absolute; left: 692px; top: 578px; width: 490px; font-size: 11px; line-height: 1.35; color: var(--ink); }
  .about strong { font-style: italic; }
  .tagline { position: absolute; left: 716px; top: 632px; font-size: 15px; font-style: italic; color: var(--ink); }

  .web-ribbon { position: absolute; left: 905px; top: 668px; font-size: 16px; font-weight: 600; color: var(--navy-deep); }

  .country { position: absolute; left: 50px; top: 722px; color: var(--white); }
  .country .name { position: absolute; left: 74px; top: 0; font-size: 36px; font-weight: 700; font-style: italic; color: var(--gold-light); line-height: 1.1; white-space: nowrap; }
  .country .pin { position: absolute; left: 30px; top: 4px; width: 36px; height: 46px; }
  .country .caption { position: absolute; left: 0; top: 58px; font-size: 18px; white-space: nowrap; }

  .stats-year { position: absolute; left: 740px; top: 720px; font-size: 30px; font-weight: 700; color: var(--white); line-height: 1; }
  .stat { position: absolute; top: 768px; color: var(--white); }
  .stat .label { font-size: 16px; font-weight: 700; font-style: italic; }
  .stat .value { font-size: 22px; font-weight: 700; margin-top: 2px; white-space: nowrap; }
  .stat.population { left: 432px; }
  .stat.gdp { left: 730px; }
  .stat.gdp .label { padding-left: 40px; }
  .stat.income { left: 978px; }
</style>
</head>
<body>
<main class="calendar-page">
  <svg class="shapes" viewBox="0 0 612 432" preserveAspectRatio="none">
    <defs>
      <linearGradient id="cityTones" x1="0" y1="0" x2="0" y2="1">
        <stop offset="0" stop-color="#4f86c6"/>
        <stop offset="0.45" stop-color="#9fb7cf"/>
        <stop offset="0.75" stop-color="#7d8a84"/>
        <stop offset="1" stop-color="#3e6a36"/>
      </linearGradient>
    </defs>
    <polygon role="img" aria-label="Photograph of the Kuala Lumpur skyline with twin towers under a blue sky" fill="url(#cityTones)" points="0,0 262,0 350,365 0,365"/>
    <polygon fill="var(--navy)" opacity="0.9" points="236,0 286,0 332,190"/>
    <polygon fill="var(--gold)" points="284,0 306,0 352,365 342,365"/>
    <path fill="var(--gold)" d="M340,258 Q470,244 612,230 L612,234 Q474,249 341,262 Z"/>
    <polygon fill="var(--gold)" points="465,340 612,340 612,358 458,358"/>
    <rect x="0" y="363" width="612" height="69" fill="var(--navy)"/>
    <rect x="0" y="363" width="212" height="69" fill="var(--navy-deep)"/>
    <polygon fill="var(--navy-deep)" points="212,366 612,366 612,386 212,386"/>
  </svg>

  <header class="month-header">
    <div class="year">2018</div>
    <div class="rule"></div>
    <div class="month">June</div>
  </header>

  <table class="month-grid">
    <thead>
      <tr><th class="weekend-col">Sun</th><th>Mon</th><th>Tue</th><th>Wed</th><th>Thu</th><th>Fri</th><th class="weekend-col">Sat</th></tr>
    </thead>
    <tbody>
      <tr><td></td><td></td><td></td><td></td><td></td><td>1</td><td class="weekend-col">2</td></tr>
      <tr><td>3</td><td>4</td><td>5</td><td>6</td><td>7</td><td>8</td><td class="weekend-col">9</td></tr>
      <tr><td>10</td><td>11</td><td>12</td><td>13</td><td>14</td><td>15</td><td class="weekend-col">16</td></tr>
      <tr><td>17</td><td>18</td><td>19</td><td>20</td><td>21</td><td>22</td><td class="weekend-col">23</td></tr>
      <tr><td>24</td><td>25</td><td>26</td><td>27</td><td>28</td><td>29</td><td class="weekend-col">30</td></tr>
    </tbody>
  </table>

  <div class="brand"><span class="mark"></span>HALVERN BRIDGE</div>
  <p class="about"><strong>Halvern Bridge</strong> was founded in 2016 to provide a wide range of management consultancy and advisory services to small and medium-sized companies operating in consumer-driven sectors.</p>
  <p class="tagline">"Working &nbsp;with you towards building a better business..."</p>

  <div class="web-ribbon">www.halvern-bridge.com</div>

  <section class="country">
    <svg class="pin" viewBox="0 0 24 30" aria-hidden="true">
      <path fill="var(--gold-light)" d="M12 0C5.4 0 0 5.2 0 11.7 0 20 12 30 12 30s12-10 12-18.3C24 5.2 18.6 0 12 0z"/>
      <circle cx="12" cy="11.5" r="4.5" fill="var(--navy-deep)"/>
    </svg>
    <div class="name">Malaysia</div>
    <div class="caption">Country's Economic Growth:</div>
  </section>

  <div class="stats-year">2017</div>
  <div class="stat population"><div class="label">Population</div><div class="value">32.08 million</div></div>
  <div class="stat gdp"><div class="label">GDP</div><div class="value">USD 336.3 billion</div></div>
  <div class="stat income"><div class="label">Per Capita Income</div><div class="value">USD 10,426.3</div></div>
</main>
</body>
</html>
```